Buddhist Center Advertisement

I need a full page single sided 8.5" by 11" flyer for posting around town that describes our upcoming schedule as well as general information about our center. The flyer should be full color and print at 300 DPI. I'm open to a variety of Buddhist imagery, but it should be related to Tibetan Buddhism.
The flyers will be read off bulletin boards so the text shouldn't be too small.
I prefer not to put text over semi-transparent graphics, I think it makes the text too difficult to read.
Target Market(s)
Spiritually minded people seeking instruction in meditation and looking for a new way of relating to themselves and the world, people looking for answers to life's most important questions. The main function of the flyer is to attract new members.
Industry/Entity Type
Town
Requirements
Must have
- 1. our schedule, with class description
Name of Module: "Walking the Path: Meeting Each Day with a Calm Heart"
In this module we will consider well the disadvantages of self-cherishing and the advantages of cherishing others more than ourselves. We will learn how to employ the special techniques of mind training or “lo-jong” as a means to transform problems into happiness, and learn to treat our challenges as precious opportunities for spiritual growth.
Saturday, September 21 10:30 - 12:30
Saturday, September 28 10:30 - 12:30
Saturday, October 26 10:30 - 12:30
Saturday, November 9 10:30 - 6:00 Retreat Day
Saturday, November 23 10:30 - 6:00 Retreat Day
2. Our website, www.velorinda-sangha.example
3. our phone number (555) 318-2046
4. Our Friendwall and Gatherup pages
https://www.social-example.com/VelorindaCenter
http://www.groups-example.com/velorinda-buddhist-center/
5. This text
"The Velorinda center is a community of spiritual friends dedicated to the practice of Tibetan Buddhism. We practice in the Gelugpa tradition, the same lineage as his Holiness The Ombar Tsendo. The Center was founded in 1994 under the spiritual direction of Geshe Tenkor Dawa, and the Society for the Continuance of the Vajrodha Heritage. We offer weekly classes in meditation and Buddhist philosophy suitable for beginners as well as advanced practitioners. All classes are free of charge and offered on a donation basis only.
Nice to have
- our logo

```html
<!DOCTYPE html>
<html lang="en">
<head>
<meta charset="utf-8">
<title>Walking the Path – Velorinda Center Flyer</title>
<link rel="stylesheet" href="https://fonts.googleapis.com/css2?family=Roboto+Condensed:wght@400;700&family=Open+Sans:ital,wght@0,400;0,700;1,700&display=swap">
<style>
  :root {
    --stage: #2e241f;
    --maroon: #7b1c1c;
    --maroon-deep: #5a1212;
    --maroon-light: #8e2a22;
    --navy: #27286a;
    --gold: #f6c20a;
    --orange: #f29a1a;
    --tan: #c3a96b;
    --ink: #111111;
    --white: #ffffff;
    --rule: #b51e1e;
  }
  * { box-sizing: border-box; margin: 0; padding: 0; }
  html, body { width: 988px; height: 1200px; overflow: hidden; }
  body { background: var(--stage); position: relative; font-family: "Open Sans", Arial, sans-serif; }

  .flyer {
    position: absolute; left: 44px; top: 18px; width: 900px; height: 1164px;
    background: linear-gradient(100deg, var(--maroon-deep) 0%, var(--maroon) 35%, var(--maroon-light) 60%, var(--maroon) 100%);
    border-bottom: 4px solid var(--rule);
    overflow: hidden;
  }

  .headline { position: absolute; left: 0; right: 0; top: 40px; text-align: center; color: var(--white);
    font-family: "Roboto Condensed", "Arial Narrow", sans-serif; font-weight: 700; text-shadow: 2px 3px 3px rgba(0,0,0,.55); }
  .headline .title { font-size: 58px; line-height: 66px; text-transform: uppercase; letter-spacing: .5px; }
  .headline .module { font-size: 44px; line-height: 56px; }

  .gallery { position: absolute; left: 0; right: 0; top: 200px; height: 233px; background: var(--navy); }
  .gallery .tile { position: absolute; top: 14px; width: 208px; height: 210px; border-radius: 10px; }
  .tile.monks { left: 20px; background: linear-gradient(160deg, #a7382a, #c98a3a 55%, #7d2a1e); }
  .tile.emblem { left: 235px; background: #f7ee2e; display: flex; align-items: center; justify-content: center; }
  .tile.statue { left: 451px; background: linear-gradient(90deg, #4a3322, #7a5a3a 50%, #1c140e); }
  .tile.teachers { left: 667px; background: linear-gradient(150deg, #9c3a2c, #d29a4c 50%, #8a2420); }
  .emblem-name { font-family: "Roboto Condensed", sans-serif; font-weight: 700; font-size: 24px; color: var(--ink); text-align: center; line-height: 28px; }
  .emblem-mark { display: block; width: 18px; height: 18px; border-radius: 50%; background: var(--ink); margin: 0 auto 10px; }

  .website { position: absolute; left: 58px; top: 466px; color: var(--gold); font-weight: 700; font-size: 30px; letter-spacing: .5px; }

  .about { position: absolute; left: 41px; top: 528px; width: 504px; height: 418px; background: var(--tan);
    border-radius: 6px; padding: 18px 20px; color: var(--ink); font-size: 16.4px; line-height: 22.4px; text-align: justify; }
  .about p + p { margin-top: 22px; }

  .schedule-day { position: absolute; right: 44px; top: 482px; color: var(--gold);
    font-family: "Roboto Condensed", sans-serif; font-weight: 700; font-size: 44px; letter-spacing: 1px; }
  .session { position: absolute; left: 574px; width: 326px; display: flex; flex-direction: column; justify-content: center;
    align-items: flex-end; padding-right: 22px; background: linear-gradient(90deg, var(--gold), var(--orange));
    clip-path: polygon(22px 0, 100% 0, 100% 100%, 22px 100%, 0 50%);
    font-family: "Roboto Condensed", sans-serif; font-weight: 700; font-size: 20px; line-height: 24px; color: var(--ink); text-transform: uppercase; }
  .session.s1 { top: 547px; height: 39px; }
  .session.s2 { top: 607px; height: 39px; }
  .session.s3 { top: 668px; height: 41px; }
  .session.s4 { top: 728px; height: 65px; }
  .session.s5 { top: 808px; height: 65px; }

  .contact { position: absolute; right: 44px; top: 904px; text-align: center; color: var(--white); font-family: "Roboto Condensed", sans-serif; }
  .contact .label { font-size: 26px; letter-spacing: 1px; }
  .contact .phone { font-size: 32px; font-weight: 700; letter-spacing: 1px; }

  .pages-bar { position: absolute; left: 0; top: 982px; width: 515px; height: 31px; background: var(--gold);
    border-radius: 0 16px 16px 0; padding-left: 42px; font-weight: 700; font-style: italic; font-size: 17px; line-height: 31px; color: var(--ink); }

  .link { position: absolute; left: 46px; display: flex; align-items: center; gap: 20px; color: var(--white); font-weight: 700; font-size: 22px; }
  .link .mark { width: 40px; height: 40px; border-radius: 6px; }
  .link.social { top: 1048px; }
  .link.social .mark { background: #3b5ca8; }
  .link.groups { top: 1095px; }
  .link.groups .mark { background: #d8261e; }
</style>
</head>
<body>
  <main class="flyer">
    <header class="headline">
      <h1 class="title">Walking the Path:</h1>
      <h2 class="module">Meeting Each Day with a Calm Heart</h2>
    </header>

    <section class="gallery">
      <div class="tile monks" role="img" aria-label="Photo of two monks in maroon robes arranging offerings"></div>
      <div class="tile emblem">
        <div class="emblem-name"><span class="emblem-mark"></span>Velorinda<br>Center</div>
      </div>
      <div class="tile statue" role="img" aria-label="Photo of a bronze Buddha statue in profile"></div>
      <div class="tile teachers" role="img" aria-label="Photo of two teachers seated together in a shrine room"></div>
    </section>

    <div class="website">www.velorinda-sangha.example</div>

    <section class="about">
      <p>The Velorinda center is a community of spiritual friends dedicated to the practice of Tibetan Buddhism. We practice in the Gelugpa tradition, the same lineage as his Holiness The Ombar Tsendo. The Center was founded in 1994 under the spiritual direction of Geshe Tenkor Dawa, and the Society for the Continuance of the Vajrodha Heritage. We offer weekly classes in meditation and Buddhist philosophy suitable for beginners as well as advanced practitioners. All classes are free of charge and offered on a donation basis only.</p>
      <p>In this module we will consider well the disadvantages of self-cherishing and the advantages of cherishing others more than ourselves. We will learn how to employ the special techniques of mind training or “lo-jong” as a means to transform problems into happiness, and learn to treat our challenges as precious opportunities for spiritual growth.</p>
    </section>

    <div class="schedule-day">SATURDAY</div>
    <div class="session s1">September 21 (10:30-12:30)</div>
    <div class="session s2">September 28 (10:30-12:30)</div>
    <div class="session s3">October 26 (10:30-12:30)</div>
    <div class="session s4"><span>November 9 (10:30-6:00)</span><span>Retreat Day</span></div>
    <div class="session s5"><span>November 23 (10:30-6:00)</span><span>Retreat Day</span></div>

    <div class="contact">
      <div class="label">CONTACT US</div>
      <div class="phone">(555) 318-2046</div>
    </div>

    <div class="pages-bar">Our Friendwall and Gatherup pages</div>
    <div class="link social"><span class="mark"></span>https://www.social-example.com/VelorindaCenter</div>
    <div class="link groups"><span class="mark"></span>http://www.groups-example.com/velorinda-buddhist-center/</div>
  </main>
</body>
</html>
```